Business Card Design Project

We are looking to redesign the logo, business card and stationary of one of our group companies - KESTRAL SUPPLY COMPANY LLC.

The company specialises in industrial PVC and CPVC Piping systems. It is situated in the Middle East and the focus is purely in this region.

The logo work is already completed. The file is uploaded for the reference.

We are looking for a clean minimalistic design for the business card.

regards
Ormund
Updates

Hello Everyone!

Thanks for submitting your designs. 

Yet to find the right design. Probably the below links will give you guys some more idea on what we would like.

Minimalist design with some creativity.

Ormund

http://plaincardgallery.example/inspiration/15-beautifully-minimal-business-cards

http://www.quietlayouthub.example/2011/11/14/30-minimalist-business-card-design/

http://www.firmpixelnotes.example/inspiration/minimal-business-cards/

Target Market(s)

Industrial users

Industry/Entity Type

Industrial

Requirements
Must have
• - Minimalistic design

- Back side of the card should include the manufacturer BRAVOLINE CANADA's decal. The file is upload for the reference

- Further information
Company Name:
KESTRAL SUPPLY COMPANY LLC
Address:
PO Box 9087, Sharjah Industrial Area 5, Qutrani Road
Sharjah, United Arab Emirates
Telephone:
+971-6-5018-392
Fax:
+977-6-5018-393
Email:
mail@ksc-holding.example

- FYI, Kestral Supply Company LLC is the authorised distributor for BRAVOLINE CANADA in the UAE. For further information on bravoline please visit the website www.bravoline.example

```html
<!DOCTYPE html>
<html lang="en">
<head>
<meta charset="utf-8">
<title>Kestral Supply Company LLC – Business Card</title>
<link rel="stylesheet" href="https://fonts.googleapis.com/css2?family=Open+Sans:wght@400;600;700&display=swap">
<style>
  :root {
    --page-bg: #e9e9e9;
    --card-dark: #353535;
    --card-glow: #4b4b4b;
    --accent-blue: #4f78c4;
    --text-white: #ffffff;
    --text-soft: #e4e4e4;
  }
  * { box-sizing: border-box; margin: 0; padding: 0; }
  html, body {
    width: 1200px;
    height: 960px;
    overflow: hidden;
    background: var(--page-bg);
    font-family: "Open Sans", sans-serif;
  }
  .canvas {
    position: relative;
    width: 1200px;
    height: 960px;
  }
  .card {
    position: absolute;
    top: 320px;
    width: 449px;
    height: 242px;
    border-radius: 18px;
    overflow: hidden;
    background: radial-gradient(ellipse at 50% 45%, var(--card-glow) 0%, var(--card-dark) 75%);
    color: var(--text-white);
  }
  .card--front { left: 106px; }
  .card--back  { left: 645px; }

  .edge-tab {
    position: absolute;
    top: 98px;
    width: 11px;
    height: 46px;
    background: var(--accent-blue);
  }
  .card--front .edge-tab { right: 0; }
  .card--back .edge-tab  { left: 0; }

  /* Front: company name */
  .brand {
    position: absolute;
    left: 108px;
    top: 86px;
    display: flex;
    align-items: center;
    gap: 14px;
  }
  .brand__mark {
    width: 56px;
    height: 56px;
    border-radius: 12px;
    background: var(--accent-blue);
  }
  .brand__name {
    font-weight: 600;
    color: var(--text-white);
    line-height: 1;
  }
  .brand__name-main {
    display: block;
    font-size: 36px;
    letter-spacing: 0.5px;
  }
  .brand__name-sub {
    display: block;
    margin-top: 4px;
    font-size: 9.5px;
    letter-spacing: 4.2px;
  }

  /* Back: contact side */
  .accent-square {
    position: absolute;
    left: 336px;
    top: 0;
    width: 120px;
    height: 118px;
    border-radius: 26px;
    background: var(--accent-blue);
  }
  .person {
    position: absolute;
    left: 36px;
    top: 26px;
  }
  .person__name {
    font-size: 23px;
    font-weight: 700;
    line-height: 1.1;
  }
  .person__title {
    font-size: 17px;
    font-weight: 400;
    color: var(--text-soft);
    line-height: 1.2;
  }
  .contact {
    position: absolute;
    left: 36px;
    top: 98px;
    list-style: none;
    font-size: 13.5px;
    line-height: 16.5px;
    color: var(--text-soft);
  }
  .contact__label { font-weight: 700; color: var(--text-white); }
  .address {
    position: absolute;
    left: 36px;
    bottom: 14px;
    font-size: 9.8px;
    color: var(--text-soft);
    white-space: nowrap;
  }
  .address__sep { margin: 0 4px; }
</style>
</head>
<body>
<main class="canvas">

  <section class="card card--front" aria-label="Card front">
    <div class="brand">
      <span class="brand__mark" aria-hidden="true"></span>
      <span class="brand__name">
        <span class="brand__name-main">KESTRAL</span>
        <span class="brand__name-sub">SUPPLY CO. LLC</span>
      </span>
    </div>
    <span class="edge-tab" aria-hidden="true"></span>
  </section>

  <section class="card card--back" aria-label="Card back">
    <span class="accent-square" aria-hidden="true"></span>
    <span class="edge-tab" aria-hidden="true"></span>
    <div class="person">
      <p class="person__name">Your Name</p>
      <p class="person__title">Managing Director</p>
    </div>
    <ul class="contact">
      <li><span class="contact__label">T:</span> +971-6-5018-392</li>
      <li><span class="contact__label">F:</span> +977-6-5018-393</li>
      <li><span class="contact__label">E:</span> mail@ksc-holding.example</li>
    </ul>
    <p class="address">PO Box 9087<span class="address__sep">|</span>Industrial Area 5, Qutrani Road<span class="address__sep">|</span>Sharjah<span class="address__sep">|</span>United Arab Emirates</p>
  </section>

</main>
</body>
</html>
```